Combining 2 Websites into 1 Website

Hi, we are merging our 2 business websites into 1 website. A little bit our business. We are a Wholesale Food Company (Kestrel Provisions PNG Ltd) with a number of retail businesses including a Deli Butchery/Bakery (named The Larko Grill Stube) and Fast Food Restaurants (Heron Wrapz, Nut Tart Tin, Wokkos) and a catering company called Larko Tana Catering. At our head office (Kestrel Provisions) we also have 2 manufacturing factories - Bakery (Larko Crust Stube products) and Butchery (Larko Fine products).
Our current websites are:
- www.kestrelprovisions-example.com.pg (mother company)
- www.grillstube-example.com.pg
We are looking to put all our brands under one website, with url www.ksv-example.com.pg . The new website will contain the following pages:
www.ksv-example.com.pg (home page)
About Us (similar look to our Kestrel Provisions Company Profile attached)
Contact (for Kestrel Provisions head office/sales)
All retail brand logos (click on a logo and be taken to that brands page)
www.ksv-example.com.pg/grillstube
o Location
o Contact
o Order Online
www.ksv-example.com.pg/heronwrapz
o Locations
o Contacts
o Order Online
www.ksv-example.com.pg/nuttarttin
o Location
o Contact
www.ksv-example.com.pg/wokkos
o Location
o Contact
o Order Online
www.ksv-example.com.pg/larkotanacatering
o Location
o Contact
www.ksv-example.com.pg/careers
o Information on how to apply for a job
o E-form that applicants complete and upload any paperwork to be sent to us? Name, DOB, Current Address, Phone Number, upload SV and Cover Letter
www.ksv-example.com.pg/shoponline
All online retails will link to this page to do an online orders (like we have setup on our Grill Stube page). Only complexity is that Delivery Charge will need to be seperate for Grill Stube products vs Heron Wrapz / Wokkos products.
Information for the Kestrel Provisions home page can be found on the attached company Profile. Information (contact, location ect) can be found on our existing Grill Stube web page).
I have attached each of our logos. I have also attached a tribal fish design (pdf) which we use on all business cards, email signatures and uniforms across all sites. Logos include (all .png files):
- Kestrel Provisions Logo
- Grill Stube Logo
- Heron Wrapz Logo
- Wokkos Logo
- Nut Tart Tin Logo
- Larko Tana Catering Logo
- Crust Stube Logo (for Kestrel Provisions - Bakery Factory Products)
- Larko Fine logo (for Kestrel Provisions - Butchery Factory Products)
- QSVRT logo (Quality Assurance cert of our Butchery Factory)
Target Market(s)
Modern, Fun, Corporate
Industry/Entity Type
Food - Manufacturing, Wholesale & Delivery, Retail, Restaurants, Catering
Coding
Coded - Design and coding required
Number of Pages Required
5+ page
Font styles to use
Look and feel

```html
<!DOCTYPE html>
<html lang="en">
<head>
<meta charset="utf-8">
<title>Kestrel Provisions PNG Ltd</title>
<link rel="stylesheet" href="https://fonts.googleapis.com/css2?family=Oswald:wght@700&family=Open+Sans:wght@400;600;700&family=Roboto:wght@500;700&display=swap">
<style>
:root{
  --red:#ed1c24;
  --red-dark:#c8141b;
  --black:#0d0d0d;
  --ink:#111;
  --grey:#6b6b6b;
  --white:#fff;
  --slate-1:#3a3d40;
  --slate-2:#202224;
  --meat:#9c1f22;
  --wood:#8a5a32;
  --pink:#f6c9cb;
}
*{box-sizing:border-box;margin:0;padding:0}
html,body{width:1200px;height:4098px;overflow:hidden;background:var(--white)}
body{font-family:"Open Sans",Arial,sans-serif;color:var(--ink)}
.page{position:relative;width:1200px;height:4098px;overflow:hidden}
.abs{position:absolute}
.layer{position:absolute;left:0;top:0}

/* nav */
.nav{left:164px;top:24px;width:872px;height:56px;background:var(--red);border-radius:28px;display:flex;align-items:center;padding:0 18px 0 22px;font-weight:700;font-size:15px;color:var(--white)}
.nav a{color:var(--white);text-decoration:none;padding:0 12px;height:56px;display:flex;align-items:center;text-transform:uppercase}
.nav a.is-active{background:var(--red-dark)}
.nav .spacer{flex:0 0 222px}
.nav .user{margin-left:auto;width:16px;height:16px}
.brand-disc{left:496px;top:-40px;width:208px;height:168px;border-radius:0 0 104px 104px;background:var(--white);display:flex;align-items:flex-end;justify-content:center;padding-bottom:40px}
.brand-disc span{font-family:"Oswald",sans-serif;font-size:20px;color:var(--red);text-transform:uppercase;text-align:center;line-height:1.1}

/* hero */
.hero-title{left:0;width:1200px;top:180px;text-align:center;font-family:"Oswald",sans-serif;font-size:70px;color:var(--white);text-transform:uppercase;letter-spacing:1px}
.hero-copy{left:280px;width:640px;top:284px;text-align:center;font-size:14px;line-height:26px;color:var(--white)}
.btn-order{left:522px;top:366px;width:156px;height:42px;border-radius:21px;background:var(--red);color:var(--white);font-weight:700;font-size:14px;display:flex;align-items:center;justify-content:center}

/* section titles */
.mark{left:578px;width:44px;height:52px;border-radius:22px 22px 4px 4px;background:var(--red);opacity:.18}
.section-title{left:0;width:1200px;text-align:center;font-family:"Oswald",sans-serif;font-size:72px;line-height:1;text-transform:uppercase}
.rule{left:560px;width:80px;height:4px;background:var(--ink)}
.story-copy{left:196px;width:808px;top:1088px;text-align:center;font-size:14px;line-height:26px;color:var(--grey)}

/* cards */
.photo-card{top:1233px;width:313px;height:355px;border:2px solid var(--white);outline:1px solid #cfcfcf}
.photo-card .fill{position:absolute;inset:0;background:linear-gradient(160deg,#5a4636,#7e1c22 55%,#2e2a26)}
.photo-card span{position:absolute;left:0;right:0;bottom:26px;text-align:center;color:var(--white);font-weight:700;font-size:21px;text-transform:uppercase}

/* brands */
.brand-badge{width:180px;height:180px;border-radius:50%;background:var(--white);display:flex;align-items:center;justify-content:center;text-align:center;padding:18px;font-family:"Oswald",sans-serif;font-size:24px;line-height:1.1;color:var(--ink);text-transform:uppercase}
.brand-badge .seal{width:96px;height:96px;border-radius:50%;background:var(--red)}

/* testimonials */
.quote-card{top:2769px;width:316px;height:298px;background:var(--white);box-shadow:0 4px 24px rgba(237,28,36,.12);padding:34px 24px 0}
.quote-card.is-focus{border:2px solid var(--red)}
.quote-card .glyph{position:absolute;left:22px;top:10px;font-family:"Oswald",sans-serif;font-size:56px;color:var(--pink);line-height:1}
.quote-card h3{position:relative;font-family:"Roboto",sans-serif;font-weight:700;font-size:18px;color:var(--ink)}
.quote-card .date{margin-top:12px;font-size:13px;font-weight:700;color:var(--red);display:flex;align-items:center;gap:6px}
.quote-card p{margin-top:18px;font-size:13.5px;line-height:26px;color:var(--grey)}

/* job form */
.job{position:absolute;left:0;top:3180px;width:1200px;height:600px;background:var(--red)}
.field{height:53px;border-radius:27px;background:var(--white);border:1px solid #f0f0f0;display:flex;align-items:center;padding:0 32px;font-size:14px;color:#777;width:318px}
.field.upload{background:var(--black);color:var(--white);font-weight:700;justify-content:center}

/* footer */
.foot-logo{left:510px;top:3700px;width:180px;height:104px;border-radius:50%;background:var(--white);border:4px solid var(--black);display:flex;align-items:center;justify-content:center;text-align:center}
.foot-logo span{font-family:"Oswald",sans-serif;font-size:20px;color:var(--ink);line-height:1.1;text-transform:uppercase}
.foot-col{top:3824px;color:var(--white)}
.foot-col h4{font-family:"Open Sans",sans-serif;font-weight:700;font-size:20px;text-transform:uppercase;line-height:1.15;margin-bottom:14px}
.foot-col p{font-size:13.5px;line-height:25px}
.foot-col ul{list-style:none;font-size:14px;line-height:25.5px}
.foot-col li::before{content:"»";margin-right:14px}
.contact-row{display:flex;align-items:center;gap:14px;font-size:14px;margin-bottom:21px}
.social{top:4042px;left:110px;display:flex;gap:10px}
.social i{width:24px;height:24px;border-radius:50%;display:block}
.copyright{right:110px;top:4046px;color:var(--white);font-size:13px;font-weight:600}
</style>
</head>
<body>
<div class="page">

  <!-- hero -->
  <svg class="layer" width="1200" height="820" viewBox="0 0 1200 820">
    <defs>
      <linearGradient id="heroShade" x1="0" y1="0" x2="0" y2="1">
        <stop offset="0" stop-color="var(--slate-1)"/>
        <stop offset=".45" stop-color="var(--slate-2)"/>
        <stop offset=".7" stop-color="var(--wood)"/>
        <stop offset="1" stop-color="var(--meat)"/>
      </linearGradient>
    </defs>
    <path d="M0 0H1200V600Q600 990 0 600Z" fill="var(--red)"/>
    <path d="M0 0H1200V575Q600 985 0 575Z" fill="url(#heroShade)" role="img" aria-label="Raw beef cuts with rosemary on wooden boards over a dark slate surface"/>
    <path d="M98 270L56 323L98 376M1102 270L1144 323L1102 376" fill="none" stroke="#fff" stroke-width="4"/>
  </svg>

  <nav class="abs nav">
    <a class="is-active" href="#">Home</a><a href="#">About Us</a><a href="#">Brand</a><a href="#">Shop</a>
    <span class="spacer"></span>
    <a href="#">Testimonials</a><a href="#">Contact Us</a>
    <svg class="user" viewBox="0 0 16 16"><circle cx="8" cy="5" r="3.2" fill="#fff"/><path d="M2 15c0-4 3-6 6-6s6 2 6 6z" fill="#fff"/></svg>
  </nav>
  <div class="abs brand-disc"><span>Kestrel<br>Provisions</span></div>

  <h1 class="abs hero-title">Kestrel Provisions</h1>
  <p class="abs hero-copy">Lorem ipsum dolor sit amet, consectetur adipiscing elit, sed do eiusmod tempor incididunt ut labore et dolore magna aliqua.</p>
  <div class="abs btn-order">ORDER NOW</div>

  <!-- our story -->
  <div class="abs mark" style="top:884px" role="img" aria-label="Flame and chef knife ornament"></div>
  <h2 class="abs section-title" style="top:952px">Our Story</h2>
  <div class="abs rule" style="top:1046px"></div>
  <p class="abs story-copy">Lorem ipsum dolor sit amet, consectetur adipiscing elit, sed do eiusmod tempor incididunt ut labore et dolore magna aliqua. Ut enim ad minim veniam, quis nostrud exercitation ullamco laboris nisi ut aliquip ex ea commodo consequat. Duis aute irure dolor in reprehenderit in voluptate velit esse cillum dolore eu fugiat nulla pariatur. Excepteur sint occaecat cupidatat non proident, sunt in culpa qui officia deserunt mollit anim id est laborum.</p>

  <!-- retail brand band -->
  <svg class="layer" width="1200" height="2520" viewBox="0 0 1200 2520">
    <defs>
      <radialGradient id="darkFood" cx=".5" cy=".45" r=".6">
        <stop offset="0" stop-color="#2a2420"/>
        <stop offset="1" stop-color="#0b0b0b"/>
      </radialGradient>
    </defs>
    <ellipse cx="600" cy="1985" rx="900" ry="510" fill="var(--red)"/>
    <ellipse cx="600" cy="1972" rx="888" ry="496" fill="url(#darkFood)" role="img" aria-label="Dim spread of grilled meats, bread and drinks on a dark table"/>
  </svg>

  <div class="abs photo-card" style="left:110px"><div class="fill" role="img" aria-label="Raw steak with broccoli, nuts and pasta"></div><span>Nemo Enim Ipsam</span></div>
  <div class="abs photo-card" style="left:443px"><div class="fill" role="img" aria-label="Sliced grilled beef with salad"></div><span>Nemo Enim Ipsam</span></div>
  <div class="abs photo-card" style="left:775px"><div class="fill" role="img" aria-label="Two raw beef cuts on a board with carving fork"></div><span>Nemo Enim Ipsam</span></div>

  <div class="abs mark" style="top:1700px" role="img" aria-label="Flame and chef knife ornament"></div>
  <h2 class="abs section-title" style="top:1766px;color:var(--white)">All Retail Brand</h2>
  <div class="abs rule" style="top:1858px;background:var(--white)"></div>

  <div class="abs brand-badge" style="left:144px;top:1915px">Larko Crust Stube</div>
  <div class="abs brand-badge" style="left:387px;top:1915px">Heron Wrapz</div>
  <div class="abs brand-badge" style="left:632px;top:1915px">Wokkos</div>
  <div class="abs brand-badge" style="left:876px;top:1915px"><div class="seal" role="img" aria-label="Quality assurance certificate badge"></div></div>
  <div class="abs brand-badge" style="left:144px;top:2133px">Grill Stube</div>
  <div class="abs brand-badge" style="left:387px;top:2133px">Larko Fine</div>
  <div class="abs brand-badge" style="left:632px;top:2133px">Nut Tart Tin</div>
  <div class="abs brand-badge" style="left:876px;top:2133px;font-size:21px">Larko Tana Catering</div>

  <!-- testimonials -->
  <div class="abs mark" style="top:2550px" role="img" aria-label="Flame and chef knife ornament"></div>
  <h2 class="abs section-title" style="top:2616px">Testimonials</h2>
  <div class="abs rule" style="top:2712px"></div>

  <svg class="abs" style="left:38px;top:2918px" width="24" height="12" viewBox="0 0 24 12"><path d="M24 6H4M8 1L2 6L8 11" fill="none" stroke="var(--ink)" stroke-width="3"/></svg>
  <svg class="abs" style="left:1122px;top:2913px" width="32" height="32" viewBox="0 0 32 32"><circle cx="16" cy="16" r="13" fill="var(--red)"/><path d="M6 16H26M21 11L27 16L21 21" fill="none" stroke="var(--ink)" stroke-width="3"/></svg>

  <div class="abs quote-card" style="left:110px">
    <span class="glyph">“</span>
    <h3>Nemo enim ipsam voluptatem</h3>
    <div class="date"><svg width="12" height="12" viewBox="0 0 12 12"><rect x="1" y="2" width="10" height="9" fill="var(--red)"/></svg>Jan 20,2022</div>
    <p>“Lorem ipsum dolor sit amet, conse cte tur adipiscing elit, sed do eiusmod temp or incididunt ut labore et dolore magna aliqua. Ut enim ad minim veniam, quis nostrud exercitation ullamco laboris nisi ex ea commodo consequat.”</p>
  </div>
  <div class="abs quote-card is-focus" style="left:442px">
    <span class="glyph">“</span>
    <h3>Nemo enim ipsam voluptatem</h3>
    <div class="date"><svg width="12" height="12" viewBox="0 0 12 12"><rect x="1" y="2" width="10" height="9" fill="var(--red)"/></svg>Jan 20,2022</div>
    <p>“Lorem ipsum dolor sit amet, conse cte tur adipiscing elit, sed do eiusmod temp or incididunt ut labore et dolore magna aliqua. Ut enim ad minim veniam, quis nostrud exercitation ullamco laboris nisi ex ea commodo consequat.”</p>
  </div>
  <div class="abs quote-card" style="left:774px">
    <span class="glyph">“</span>
    <h3>Nemo enim ipsam voluptatem</h3>
    <div class="date"><svg width="12" height="12" viewBox="0 0 12 12"><rect x="1" y="2" width="10" height="9" fill="var(--red)"/></svg>Jan 20,2022</div>
    <p>“Lorem ipsum dolor sit amet, conse cte tur adipiscing elit, sed do eiusmod temp or incididunt ut labore et dolore magna aliqua. Ut enim ad minim veniam, quis nostrud exercitation ullamco laboris nisi ex ea commodo consequat.”</p>
  </div>

  <!-- careers -->
  <section class="job"></section>
  <div class="abs mark" style="top:3222px;background:var(--white);opacity:.35" role="img" aria-label="Flame and chef knife ornament"></div>
  <h2 class="abs section-title" style="top:3292px;color:var(--white)">How to Apply for a Job</h2>
  <div class="abs rule" style="top:3392px;background:var(--white)"></div>

  <div class="abs field" style="left:110px;top:3444px">Name</div>
  <div class="abs field" style="left:442px;top:3444px;justify-content:space-between">Dob<svg width="13" height="13" viewBox="0 0 13 13"><rect x="1" y="2" width="11" height="10" fill="none" stroke="#888" stroke-width="1.5"/><path d="M1 5H12" stroke="#888" stroke-width="1.5"/></svg></div>
  <div class="abs field" style="left:772px;top:3444px">Current Address</div>
  <div class="abs field" style="left:110px;top:3521px">Phone</div>
  <div class="abs field" style="left:442px;top:3521px">Email</div>
  <div class="abs field upload" style="left:772px;top:3521px">UPLOAD SV</div>

  <!-- footer -->
  <svg class="abs" style="left:0;top:3620px" width="1200" height="478" viewBox="0 0 1200 478">
    <path d="M0 100Q600 -60 1200 100V478H0Z" fill="var(--white)"/>
    <path d="M0 140Q600 -20 1200 140V478H0Z" fill="var(--black)"/>
  </svg>
  <div class="abs foot-logo"><span>Kestrel<br>Provisions</span></div>

  <div class="abs foot-col" style="left:110px;width:250px">
    <h4>Kestrel Provisions<br>PNG Ltd</h4>
    <p>Lorem ipsum dolor sit amet, conse ctetur adipiscing elit, sed do eiusmod tempor incididunt ut labore et dolor e magna aliqua.</p>
  </div>
  <div class="abs foot-col" style="left:410px">
    <h4>Sitemap</h4>
    <ul><li>Home</li><li>Membership</li><li>Events</li><li>Resources</li><li>Contact Us</li></ul>
  </div>
  <div class="abs foot-col" style="left:645px">
    <h4>Information</h4>
    <ul><li>About Us</li><li>Faq</li><li>Services</li><li>Latest News</li><li>Partners</li></ul>
  </div>
  <div class="abs foot-col" style="left:869px">
    <h4>Contact Us</h4>
    <div class="contact-row"><svg width="12" height="14" viewBox="0 0 12 14"><path d="M6 0a5 5 0 0 0-5 5c0 4 5 9 5 9s5-5 5-9a5 5 0 0 0-5-5z" fill="var(--red)"/><circle cx="6" cy="5" r="2" fill="var(--black)"/></svg>123, Lorem ipsum dolor sit</div>
    <div class="contact-row"><svg width="13" height="13" viewBox="0 0 13 13"><path d="M3 0l2 3-1.5 1.5a8 8 0 0 0 5 5L10 8l3 2-1.5 3C6 13 0 7 0 1.5z" fill="var(--red)"/></svg>+1 888 888 8888</div>
    <div class="contact-row"><svg width="14" height="11" viewBox="0 0 14 11"><rect width="14" height="11" fill="var(--red)"/><path d="M0 0l7 6 7-6" fill="none" stroke="var(--black)" stroke-width="1.5"/></svg>info@example-mail.com</div>
  </div>

  <div class="abs social">
    <i style="background:#3b5998"></i><i style="background:#1da1f2"></i><i style="background:#dd4b39"></i><i style="background:#e60023"></i>
  </div>
  <div class="abs copyright">© Copyrights 2022 Company name | All Rights reserved</div>
</div>
</body>
</html>
```